Informational Landing Page Redesign

Purebrook Filter Guide, reviews and provides information about water ionizers for users. The web site is supposed to be an "expert or researched based" We are looking to redesign the following landing page:

http://www.purebrookfilterguide-example.com/learn/what-is-pure-flow

The design should be geared towards converting visitors into leads. We are looking for a redesign of the content section. The header and footer should be the same as the current site. The text and colors should be consistent with the current site but please feel free to make bold choices that work and add stock photos.

Target Market(s)

Ages 45+ with disposable income.

Industry/Entity Type

Learn

Requirements
Must have
• The page must have the all current content. It also should have a web site form placed above the fold.

Please note you can change the designs of the "advertisements".
Nice to have
• Placement of social media elements so users can spread the page to friends, example facebook and google+ like buttons. A banner area that is capable of holding a rotating banner or video or banner.
Should not have
• Distractions from the goal, converting users to leads.
Distractions from the content, since the user is there to read.
Missing information and text, all information on the current page should appear on the redesign.

Deviations from the current header and footer.

```html
<!DOCTYPE html>
<html lang="en">
<head>
<meta charset="utf-8">
<title>What is Alkaline Water? | Purebrook Filter Guide</title>
<link href="https://fonts.googleapis.com/css2?family=Arimo:wght@400;700&family=Bitter:wght@700&family=Open+Sans:ital,wght@0,400;0,600;0,700;1,700;1,800&display=swap" rel="stylesheet">
<style>
:root{
  --page:#efeeec;
  --ink:#3a3a3a;
  --heading:#333;
  --logo-grey:#6b6b6b;
  --brand-blue:#2a8fd5;
  --link:#1f7fc8;
  --orange:#f28a12;
  --red:#c0171b;
}
*{box-sizing:border-box;margin:0;padding:0}
html,body{width:1024px;height:1200px;overflow:hidden}
body{background:var(--page);font-family:Arimo,Arial,sans-serif;color:var(--ink);position:relative}
.abs{position:absolute}

/* header */
.brand{left:176px;top:18px;display:flex;align-items:center;gap:10px}
.brand-dot{width:40px;height:40px;border-radius:50%;background:var(--brand-blue);flex:none}
.brand-name{font:700 20px/21px "Open Sans",sans-serif;color:var(--logo-grey);letter-spacing:.3px;text-transform:uppercase}
.brand-tag{left:233px;top:64px;font:400 11px "Open Sans",sans-serif;color:#666}
.social{left:712px;top:20px;display:flex;gap:7px}
.social span{width:29px;height:29px;border-radius:4px;display:block}

.nav{left:0;top:96px;width:1024px;height:29px;background:linear-gradient(#3a9be0,#1f82cc);border-top:1px solid #5aaee8}
.nav ul{list-style:none;display:flex;position:absolute;left:194px;top:6px}
.nav li{font:700 12px "Open Sans",sans-serif;color:#fff;margin-right:32px}
.buyers{left:755px;top:98px;width:87px;height:24px;background:linear-gradient(#ffa12c,#ef7f06);border-radius:3px;color:#fff;font:700 11px/24px "Open Sans",sans-serif;text-align:center}

/* banner */
.banner{left:0;top:125px;width:1024px;height:184px;background:linear-gradient(90deg,#2a7fc0,#5db0e6 20%,#3a8fd0 50%,#5db0e6 80%,#2a7fc0)}
.banner-photo{left:174px;top:125px;width:682px;height:184px;background:linear-gradient(100deg,#2e8a6a,#79c0a8 35%,#a9dcec 60%,#3f97c9)}
.banner-card{left:202px;top:137px;width:276px;height:162px;background:rgba(40,70,80,.55)}
.banner-title{left:224px;top:146px;font:italic 700 23px/26px "Open Sans",sans-serif;color:#8fd8ff}
.banner-title span{display:block;padding-left:45px}
.banner-copy{left:214px;top:203px;width:256px;font:700 11.5px/16px Arimo,sans-serif;color:#fff}
.banner-btn{left:388px;top:263px;width:74px;height:21px;border-radius:3px;background:linear-gradient(#43b2f2,#1579c9);color:#fff;font:700 10px/21px Arimo,sans-serif;text-align:center}
.arrow{top:194px;width:24px;height:34px}
.dots{left:498px;top:293px;display:flex;gap:4px}
.dots span{width:11px;height:11px;background:#555;color:#ddd;font:8px/11px Arimo;text-align:center}
.dots span.on{background:#eee;color:#333}
.shade{left:0;top:309px;width:1024px;height:30px;background:linear-gradient(#d3d3d2,var(--page))}

/* content */
.main{left:173px;top:332px;width:473px}
.main h1{font:700 23px "Bitter",serif;color:var(--heading);margin-bottom:10px}
.main p{font-size:12.4px;line-height:15.6px;text-align:justify;margin-bottom:14px}
.main p.intro{font-size:12.5px;letter-spacing:.4px}
.chart{width:472px;height:262px;border:3px solid #bfbfbf;border-radius:3px;box-shadow:0 8px 10px rgba(0,0,0,.25);margin:16px 0 26px;background:linear-gradient(90deg,#fbeaea,#fdf6e6 22%,#eef8ea 45%,#eaf0fb 60%,#f3eafb 80%,#fbe9f2)}
.main ul{list-style:none;margin:-2px 0 10px 8px}
.main li{font-size:12.4px;line-height:19.5px;padding-left:16px;position:relative}
.main li:before{content:"";position:absolute;left:0;top:5px;width:9px;height:9px;border-radius:50%;border:1px solid #999}

/* sidebar */
.box{left:665px;width:190px;background:linear-gradient(90deg,#dcdddf,#f4f4f4 60%,#e2e3e4);border:1px solid #cfcfcf;border-radius:3px;box-shadow:0 6px 6px rgba(0,0,0,.12)}
.ribbon{position:absolute;left:16px;top:-4px;width:156px;height:40px;background:linear-gradient(#4fb3ee,#1a78c4);border-radius:0 0 60px 60px/0 0 14px 14px;color:#fff;font:italic 800 15px/36px "Open Sans",sans-serif;text-align:center;border-top:5px solid #24374a}
.ribbon.two{line-height:14px;padding-top:5px;height:46px}
.box h4{position:absolute;left:0;width:100%;text-align:center;font:italic 800 13.5px/16px "Open Sans",sans-serif;color:var(--link)}
.field{position:absolute;left:16px;width:158px;height:19px;background:#fff;border:1px solid #d4d4d4;border-radius:2px;font:9px/17px Arimo;color:#666;padding-left:8px}
.btn{position:absolute;left:29px;width:132px;height:27px;border-radius:4px;background:linear-gradient(#45b4f3,#1672c5);color:#fff;font:600 13px/27px "Open Sans",sans-serif;text-align:center}
.learn-links{position:absolute;left:28px;top:37px;width:136px;list-style:none}
.learn-links li{font:600 11px/21px "Open Sans",sans-serif;color:var(--link);border-bottom:1px dashed #999;letter-spacing:-.2px}
.learn-links li:last-child{border:0}
.ph-area{position:absolute;border:2px solid #fff}

/* footer */
.foot-rule{left:173px;top:1122px;width:682px;height:1px;background:#cfcfcf}
.foot-brand{left:176px;top:1136px}
.foot-brand .brand-name{font-size:17px;line-height:19px}
.foot-tag{left:233px;top:1178px}
.copy{left:466px;top:1136px;font-size:10px;color:#333}
.copy a{color:var(--link);text-decoration:none}
.foot-nav{left:463px;top:1155px;display:flex;font-size:11px}
.foot-nav span{color:var(--link);padding:0 9px;border-left:1px solid #ccc}
.foot-nav span:first-child{border:0;padding-left:0}
</style>
</head>
<body>

<header>
  <div class="abs brand"><span class="brand-dot"></span><span class="brand-name">Purebrook Filter<br>Guide</span></div>
  <div class="abs brand-tag">Find the perfect Water Ionizer.</div>
  <div class="abs social" aria-label="Social sharing">
    <span style="background:#3b5998"></span><span style="background:#b8261e"></span><span style="background:#33b6e6"></span><span style="background:#c9332a"></span>
  </div>
</header>

<nav class="abs nav"><ul><li>HOME</li><li>REVIEWS</li><li>LEARN</li><li>COMPARE</li><li>BLOG</li><li>ABOUT US</li></ul></nav>
<div class="abs buyers">Buyer's Guide</div>

<section class="banner-area">
  <div class="abs banner"></div>
  <div class="abs banner-photo" role="img" aria-label="Water ionizer machine standing on fresh green grass with water drops"></div>
  <div class="abs banner-card"></div>
  <div class="abs banner-title">Lorem ipsum dolor<span>Consectetuer adip</span></div>
  <div class="abs banner-copy">Lorem ipsum dolor sit amet, consectetuer adipiscing elit. Nam cursus. Morbi ut mi. Nulla enim leo, egestas id, condimentum at, laoreet</div>
  <div class="abs banner-btn">Learn more</div>
  <svg class="abs arrow" style="left:176px" viewBox="0 0 24 34"><path d="M20 3 5 17l15 14" fill="none" stroke="#fff" stroke-width="5"/></svg>
  <svg class="abs arrow" style="left:826px" viewBox="0 0 24 34"><path d="M4 3l15 14L4 31" fill="none" stroke="#fff" stroke-width="5"/></svg>
  <div class="abs dots"><span>1</span><span class="on">2</span><span>3</span><span>4</span></div>
  <div class="abs shade"></div>
</section>

<main class="abs main">
  <h1>What is Alkaline Water?</h1>
  <p class="intro">The Water Ionizer industry is chalked full of confusing information. They often throw around machine specifications and technical jargon that needs to be dissected and explained in order to be understood. Our team at Purebrook Filter Guide is hoping to avoid this by giving you only the facts you need. We have written this information coherently so you may understand the properties of alkaline water and how it benefits you. We want your next Water Ionizer purchase to be clear and informed. So let’s start with the basics, what exactly is alkaline water?</p>

  <div class="chart" role="img" aria-label="Infographic of the pH scale from 0 to 14 with example solutions for each value"></div>

  <p>Simply put, alkaline water is water with a potential hydrogen (pH) value of more than 7 (7 being neutral on the pH scale). Typically in the water ionizer industry, this is achieved using a process known as “electrodialysis”. This process splits the neutral water into 2 types, acidic and alkaline. Both have their unique benefits and properties, but alkaline water is filled with healthy minerals like:</p>
  <ul><li>Calcium</li><li>Magnesium</li><li>Potassium</li></ul>
  <p>While unhealthy minerals like fluoride, nitrates, and sulfides, are flushed out through the acidic water.</p>
  <p>Besides the ability to eliminate the harmful toxins that are found in most tap water, there are numerous health benefits to alkaline water – all of which are backed by research. Leaders in the health and fitness industry have attested to the advantages of alkaline water for years. Maybe it’s time you discovered the real power of Alkaline Water for yourself?</p>
</main>

<aside>
  <div class="abs box" style="top:318px;height:194px">
    <div class="ribbon">START HERE!</div>
    <h4 style="top:46px">DOWNLOAD YOUR FREE<br>BUYER'S GUIDE NOW!</h4>
    <div class="field" style="top:85px">Name</div>
    <div class="field" style="top:110px">E-mail</div>
    <div class="field" style="top:135px">Phone</div>
    <div class="btn" style="top:159px">Download</div>
  </div>

  <div class="abs box" style="top:530px;height:172px">
    <div class="ribbon">LEARN</div>
    <ul class="learn-links">
      <li>What is Alkaline Water?</li><li>Benefits of Alkaline Water</li><li>What is Acidic Water?</li><li>Benefits of Acidic Water</li><li>What are pH and ORP?</li><li>How do Ionizers work?</li>
    </ul>
  </div>

  <div class="abs box" style="top:718px;height:182px">
    <div class="ribbon two">ALKALINE<br>LIFESTYLE</div>
    <div class="ph-area" role="img" aria-label="Video still of a presenter beside a sunny coastal boardwalk" style="left:27px;top:52px;width:136px;height:82px;background:linear-gradient(100deg,#c9a37a,#e8cf9a 45%,#9cb9c9)"></div>
    <div class="btn" style="top:142px;height:25px;line-height:25px">Join Today!</div>
  </div>

  <div class="abs box" style="top:918px;height:179px">
    <div class="ribbon two" style="font-size:12px">Find the best deals on<br>water IonizerS</div>
    <div class="ph-area" role="img" aria-label="Three countertop water ionizer units" style="left:26px;top:52px;width:80px;height:66px;border:0;background:linear-gradient(90deg,#d8d8d8,#3a3a3a 55%,#9a9a9a)"></div>
    <div style="position:absolute;left:94px;top:44px;font:italic 800 14px/16px 'Open Sans',sans-serif;color:var(--red)">GURANTEED</div>
    <div style="position:absolute;left:96px;top:62px;width:80px;text-align:right;font:italic 700 11.5px/14px 'Open Sans',sans-serif;color:#222">Talk to expert<br>today!</div>
    <div style="position:absolute;left:0;width:100%;top:128px;text-align:center;font:italic 800 17px 'Open Sans',sans-serif;color:var(--red)">(800) 555-0142</div>
    <div style="position:absolute;left:0;width:100%;top:152px;text-align:center;font:400 12px 'Open Sans',sans-serif;color:var(--link)">PurebrookAdvisor.com</div>
  </div>
</aside>

<footer>
  <div class="abs foot-rule"></div>
  <div class="abs brand foot-brand"><span class="brand-dot"></span><span class="brand-name">Purebrook Filter<br>Guide</span></div>
  <div class="abs brand-tag foot-tag">Find the perfect Water Ionizer.</div>
  <div class="abs copy">© 2009-2012 Purebrook Filter Guide. All Rights Reserved | Read our <a>Privacy Policy</a>.</div>
  <div class="abs foot-nav"><span>Home</span><span>Reviews</span><span>Learn</span><span>Compare</span><span>Blog</span><span>About Us</span><span>Buyer’s Guide</span></div>
</footer>

</body>
</html>
```